QLindex warden tap - styling

We have a prototyped single page application. The content is in place what we need is restyling to

- make it more user friendly
- modern look and feel
- improve accessibility features
- use our brand guidelines (screen shots attached of the full website)

Prototype is available at http://boardviewapp.examplehost.net/

Target form factor:
Primary - tablet
Secondary - desktop

Target Market(s)

Business users - not financial professionals but people working for big companies who have some limited training in the concepts

Number of Pages Required

1 page

Requirements
Must have
• Touch user interface

```html
<!DOCTYPE html>
<html lang="en">
<head>
<meta charset="utf-8">
<title>QLindex warden tap – Flight Plan</title>
<link rel="stylesheet" href="https://fonts.googleapis.com/css2?family=Arimo:wght@400;700&display=swap">
<style>
  :root {
    --page-bg: #e3e3e3;
    --frame-bg: #d9d9d9;
    --brand: #a3135f;
    --brand-dark: #98115a;
    --brand-deep: #7d0c4a;
    --stat-bg: #9b9b9b;
    --stat-active: #5b5b5b;
    --white: #ffffff;
    --ink: #3a3a3a;
    --axis-ink: #5a5a5a;
    --grid: #c9ccd1;
    --history: #8ccbee;
    --plan: #7a3a78;
    --fan-outer: #e9f3fc;
    --fan-inner: #d3e8f8;
    --median: #8ab8dc;
    --panel-border: #c8c8c8;
  }
  * { box-sizing: border-box; margin: 0; padding: 0; }
  html, body { width: 1200px; height: 850px; overflow: hidden; }
  body { background: var(--page-bg); font-family: "Arimo", Arial, sans-serif; position: relative; }

  .app-frame { position: absolute; left: 84px; top: 55px; width: 1030px; height: 732px; background: var(--frame-bg); }

  .top-bar { position: absolute; left: 100px; top: 71px; width: 1000px; height: 88px; background: var(--brand); border-radius: 4px; overflow: hidden; }
  .brand-block { position: absolute; left: 0; top: 0; width: 212px; height: 88px; background: var(--brand-dark); display: flex; align-items: center; padding-left: 48px; }
  .brand-name { color: var(--white); font-weight: 700; font-size: 32px; letter-spacing: -1px; }
  .company-menu { position: absolute; right: 22px; top: 0; height: 88px; display: flex; align-items: center; gap: 24px; }
  .company-item { display: flex; align-items: center; gap: 14px; color: var(--white); font-weight: 700; font-size: 15px; }
  .company-item .caret { width: 20px; height: 20px; border-radius: 50%; background: var(--brand-deep); display: flex; align-items: center; justify-content: center; }

  .stat-row { position: absolute; left: 100px; top: 172px; width: 1000px; height: 60px; display: flex; border-radius: 4px 4px 0 0; overflow: visible; }
  .stat { flex: 1; background: var(--stat-bg); color: var(--white); text-align: center; padding-top: 11px; border-right: 1px solid #b6b6b6; position: relative; }
  .stat:first-child { border-radius: 4px 0 0 0; }
  .stat:last-child { border-right: none; border-radius: 0 4px 0 0; }
  .stat-value { font-size: 23px; font-weight: 700; line-height: 24px; }
  .stat-label { font-size: 11px; font-weight: 700; letter-spacing: .3px; margin-top: 1px; }
  .stat.is-active { background: var(--stat-active); }
  .stat.is-active::after { content: ""; position: absolute; left: 116px; bottom: -7px; border: 7px solid transparent; border-bottom: 0; border-top-color: var(--stat-active); }

  .flight-panel { position: absolute; left: 100px; top: 238px; width: 1000px; height: 459px; background: var(--white); border: 2px solid var(--panel-border); border-radius: 4px; }
  .panel-head { height: 56px; background: linear-gradient(#ececec, #d3d3d3); display: flex; align-items: center; padding-left: 20px; font-weight: 700; font-size: 16px; letter-spacing: .8px; color: var(--ink); position: relative; }
  .collapse-btn { position: absolute; right: 22px; top: -2px; width: 26px; height: 20px; background: var(--brand); border-radius: 0 0 4px 4px; display: flex; align-items: center; justify-content: center; }
  .chart { position: absolute; left: 1px; top: 56px; }
  .axis-label { font-size: 11px; fill: var(--axis-ink); font-family: "Arimo", Arial, sans-serif; }

  .control-bar { position: absolute; left: 103px; top: 711px; width: 997px; height: 58px; background: var(--brand); border-radius: 29px; }
  .control { position: absolute; top: 0; height: 58px; color: var(--white); }
  .control-title { position: absolute; top: 4px; width: 100%; text-align: center; font-weight: 700; font-size: 13px; letter-spacing: .5px; }
  .track { position: absolute; top: 24px; left: 0; right: 0; height: 9px; border-radius: 5px; background: linear-gradient(#ffffff, #d8d8d8); }
  .knob { position: absolute; top: 17px; width: 24px; height: 22px; margin-left: -12px; }
  .scale { position: absolute; top: 37px; left: 0; right: 0; display: flex; justify-content: space-between; font-size: 12px; font-weight: 700; }
  .strategy { left: 30px; width: 448px; }
  .contributions { left: 519px; width: 448px; }
</style>
</head>
<body>
  <div class="app-frame"></div>

  <header class="top-bar">
    <div class="brand-block"><span class="brand-name">QLindex</span></div>
    <nav class="company-menu" aria-label="Company selectors">
      <div class="company-item">XYZ Limited <span class="caret"><svg width="10" height="7" viewBox="0 0 10 7"><path d="M0 0h10L5 7z" fill="#c9468c"/></svg></span></div>
      <div class="company-item">XYZ Limited <span class="caret"><svg width="10" height="7" viewBox="0 0 10 7"><path d="M0 0h10L5 7z" fill="#c9468c"/></svg></span></div>
      <div class="company-item">XYZ Limited <span class="caret"><svg width="10" height="7" viewBox="0 0 10 7"><path d="M0 0h10L5 7z" fill="#c9468c"/></svg></span></div>
      <div class="company-item">XYZ Limited <span class="caret"><svg width="10" height="7" viewBox="0 0 10 7"><path d="M0 0h10L5 7z" fill="#c9468c"/></svg></span></div>
    </nav>
  </header>

  <section class="stat-row" aria-label="Key figures">
    <div class="stat"><div class="stat-value">91%</div><div class="stat-label">FUNDING LEVEL</div></div>
    <div class="stat"><div class="stat-value">-1.7%</div><div class="stat-label">FUNDING LEVEL CHANGE</div></div>
    <div class="stat"><div class="stat-value">-10.5%</div><div class="stat-label">PROGRESS AGAINES FLIGHT PLAN</div></div>
    <div class="stat is-active"><div class="stat-value">67%</div><div class="stat-label">10 YR PROJECTED FUNDING LEVEL</div></div>
  </section>

  <section class="flight-panel">
    <div class="panel-head">FLIGHT PLAN
      <span class="collapse-btn"><svg width="10" height="7" viewBox="0 0 10 7"><path d="M1 6l4-4 4 4" stroke="#fff" stroke-width="2" fill="none"/></svg></span>
    </div>
    <svg class="chart" width="995" height="399" viewBox="103 296 995 399" role="img" aria-label="Funding level history and projection chart">
      <g stroke="var(--grid)" stroke-width="1">
        <line x1="157" y1="347" x2="1090" y2="347"/>
        <line x1="157" y1="413" x2="1090" y2="413"/>
        <line x1="157" y1="479" x2="1090" y2="479"/>
        <line x1="157" y1="545" x2="1090" y2="545"/>
        <line x1="157" y1="610" x2="1090" y2="610" stroke="#b5cde0"/>
      </g>
      <g class="axis-label" text-anchor="end">
        <text x="144" y="351">140%</text>
        <text x="144" y="417">120%</text>
        <text x="144" y="483">100%</text>
        <text x="144" y="549">80%</text>
        <text x="144" y="614">60%</text>
      </g>
      <polygon fill="var(--fan-outer)" points="676,508 720,466 780,443 900,415 1010,398 1090,391 1090,560 900,551 770,545 720,530"/>
      <polygon fill="var(--fan-inner)" points="676,508 720,500 800,487 900,472 1000,457 1090,446 1090,515 900,516 800,517 720,520"/>
      <line x1="676" y1="508" x2="1090" y2="481" stroke="var(--median)" stroke-width="1"/>
      <polyline fill="none" stroke="var(--history)" stroke-width="2" points="168,512 180,511 195,513 210,511 225,509 240,511 255,511 270,510 285,512 300,511 312,515 318,510 330,510 345,508 360,507 375,508 390,508 405,507 420,511 435,509 450,508 462,506 475,509 490,510 505,509 520,508 535,509 550,509 565,510 580,509 595,509 610,507 625,507 640,508 655,509 676,508"/>
      <line x1="338" y1="507" x2="1090" y2="475" stroke="var(--plan)" stroke-width="3"/>
      <g stroke="#b5cde0">
        <line x1="168" y1="610" x2="168" y2="616"/><line x1="317" y1="610" x2="317" y2="616"/><line x1="458" y1="610" x2="458" y2="616"/><line x1="604" y1="610" x2="604" y2="616"/><line x1="676" y1="610" x2="676" y2="616"/><line x1="725" y1="610" x2="725" y2="616"/><line x1="778" y1="610" x2="778" y2="616"/><line x1="833" y1="610" x2="833" y2="616"/><line x1="890" y1="610" x2="890" y2="616"/><line x1="950" y1="610" x2="950" y2="616"/><line x1="1012" y1="610" x2="1012" y2="616"/><line x1="1076" y1="610" x2="1076" y2="616"/>
      </g>
      <g class="axis-label" text-anchor="middle">
        <text x="168" y="630">29/Nov/13</text><text x="317" y="630">30/Jan/14</text><text x="458" y="630">30/Mar/14</text><text x="604" y="630">30/May/14</text><text x="676" y="630">2014</text><text x="725" y="630">2015</text><text x="778" y="630">2016</text><text x="833" y="630">2017</text><text x="890" y="630">2018</text><text x="950" y="630">2019</text><text x="1012" y="630">2020</text><text x="1076" y="630">2021</text>
      </g>
      <circle cx="591" cy="654" r="6" fill="var(--brand)"/>
      <circle cx="609" cy="654" r="6" fill="#9b9b9b"/>
    </svg>
  </section>

  <section class="control-bar" aria-label="Scenario controls">
    <div class="control strategy">
      <div class="control-title">INVESTMENT STRATEGY</div>
      <div class="track"></div>
      <svg class="knob" style="left:224px" viewBox="0 0 24 22"><path d="M12 0L24 11 12 22 0 11z" fill="#e8175d" stroke="#7d0c4a"/><path d="M4 11h16" stroke="#7d0c4a"/></svg>
      <div class="scale"><span>Matching</span><span>Matching</span><span>Growth</span></div>
    </div>
    <div class="control contributions">
      <div class="control-title">CONTRIBUTIONS</div>
      <div class="track"></div>
      <svg class="knob" style="left:203px" viewBox="0 0 24 22"><path d="M12 0L24 11 12 22 0 11z" fill="#e8175d" stroke="#7d0c4a"/><path d="M4 11h16" stroke="#7d0c4a"/></svg>
      <div class="scale"><span>£0.00m</span><span>£6.0m</span><span>£12.00m</span></div>
    </div>
  </section>
</body>
</html>
```